Business Card Design

We Import cars and commercial vehicles, we have been in business around 12 years, we are based in Christchurch, New Zealand.
I really like the web address on card, possibly right along the bottom of the card?
We specialize in commercial vans, maybe worth a mention?
The logo has the name in it so probably don't need to have twice?

I really like a clean smart look, not too cluttered

Industry/Entity Type

Business

Contact Information for Business Card

RQL TOKYO IMPORTS, Derek Holloway, Managing Director
web address: www.rqlmotorsnz.com
cell phone. 021 485 912

Requirements
Must have
• the logo, and all the contact details.

Forgot to add my email address, derek@rqlmotorsnz.com
Nice to have
• Just thinking as the card is looking a little empty maybe somewhere written what we do? 'Specializing in commercial vans'
Not sure but we import Japanese vehicles, possibly adding some brands like Velkara Poremo Ketsu Brivon etc? Not sure on that one.

```html
<!DOCTYPE html>
<html lang="en">
<head>
<meta charset="utf-8">
<title>RQL Tokyo Imports – Business Card</title>
<link rel="stylesheet" href="https://fonts.googleapis.com/css2?family=Crimson+Text:ital,wght@0,400;0,700;1,400;1,700&display=swap">
<style>
  :root {
    --backdrop: #1d2224;
    --card-white: #ffffff;
    --card-black: #050505;
    --ink: #111111;
    --ink-light: #f2f2f2;
    --link-blue: #3fa6df;
    --van-light: #e6e8ea;
    --van-dark: #6e7377;
  }
  * { box-sizing: border-box; margin: 0; padding: 0; }
  html, body {
    width: 1200px;
    height: 722px;
    overflow: hidden;
    background: var(--backdrop);
    font-family: "Crimson Text", "Times New Roman", serif;
  }
  .card {
    position: absolute;
    left: 110px;
    top: 81px;
    width: 980px;
    height: 560px;
    background: var(--card-black);
    overflow: hidden;
    box-shadow: 0 18px 40px rgba(0,0,0,0.45);
  }
  .card__split {
    position: absolute;
    inset: 0;
    width: 100%;
    height: 100%;
  }
  .brand {
    position: absolute;
    left: 62px;
    top: 128px;
    width: 420px;
    color: var(--ink);
  }
  .brand__name {
    font-weight: 700;
    font-size: 58px;
    line-height: 0.95;
    letter-spacing: 1px;
    color: var(--ink);
  }
  .brand__tagline {
    margin-top: 22px;
    font-style: italic;
    font-weight: 700;
    font-size: 27px;
    color: var(--ink);
  }
  .van-artwork {
    position: absolute;
    left: 392px;
    top: 66px;
    width: 160px;
    height: 92px;
    border-radius: 18px 26px 10px 10px;
    background: linear-gradient(160deg, var(--van-light) 0%, #c5c9cc 55%, var(--van-dark) 100%);
  }
  .contact {
    position: absolute;
    right: 70px;
    top: 232px;
    width: 330px;
    color: var(--ink-light);
    text-align: right;
  }
  .contact__name {
    font-style: italic;
    font-size: 29px;
    line-height: 1.1;
    padding-right: 10px;
  }
  .contact__role {
    font-style: italic;
    font-size: 21px;
    padding-right: 10px;
    margin-bottom: 26px;
  }
  .contact__line {
    display: flex;
    justify-content: flex-end;
    align-items: center;
    gap: 18px;
    font-size: 22px;
    line-height: 1.55;
  }
  .contact__icon {
    width: 26px;
    height: 20px;
    flex: none;
  }
  .website {
    position: absolute;
    left: 340px;
    top: 478px;
    font-style: italic;
    font-size: 30px;
    color: var(--link-blue);
    letter-spacing: 0.5px;
  }
</style>
</head>
<body>
  <main class="card">
    <svg class="card__split" viewBox="0 0 980 560" preserveAspectRatio="none" aria-hidden="true">
      <polygon points="0,0 980,0 0,560" fill="var(--card-white)"/>
    </svg>

    <div class="van-artwork" role="img" aria-label="Illustration of a white commercial van"></div>

    <section class="brand">
      <h1 class="brand__name">RQL TOKYO<br>IMPORTS</h1>
      <p class="brand__tagline">Specializing in commercial vans</p>
    </section>

    <section class="contact">
      <p class="contact__name">Derek Holloway</p>
      <p class="contact__role">Managing Director</p>
      <p class="contact__line">
        <span>021 485 912</span>
        <svg class="contact__icon" viewBox="0 0 26 20" aria-label="Phone">
          <path d="M2 7 C2 2 24 2 24 7 L24 9 L18 9 L18 6 L8 6 L8 9 L2 9 Z" fill="var(--ink-light)"/>
          <path d="M7 10 L19 10 L22 18 L4 18 Z" fill="var(--ink-light)"/>
          <circle cx="13" cy="14" r="2.6" fill="var(--card-black)"/>
        </svg>
      </p>
      <p class="contact__line">
        <span>derek@rqlmotorsnz.com</span>
        <svg class="contact__icon" viewBox="0 0 26 20" aria-label="Email">
          <rect x="2" y="3" width="22" height="15" fill="var(--ink-light)"/>
          <path d="M2 3 L13 12 L24 3" fill="none" stroke="var(--card-black)" stroke-width="1.6"/>
        </svg>
      </p>
    </section>

    <p class="website">www.rqlmotorsnz.com</p>
  </main>
</body>
</html>
```